Lanternleaf - Fresh Asian Cuisine Menu

We need to redo our menu to include pictures of food items. Our restaurant is vibrant, trendy, upscale Chinese cuisine

Requirements
Must have
• Must fit on 8.5x11 paper. We can remove the About Us section if needed but menu cannot be more than 6 pages total. Must include pictures of menu items

```html
<!DOCTYPE html>
<html lang="en">
<head>
<meta charset="utf-8">
<title>Lanternleaf - Fresh Asian Cuisine | Appetizers</title>
<link rel="stylesheet" href="https://fonts.googleapis.com/css2?family=Cinzel:wght@700&family=Arimo:wght@400&display=swap">
<style>
  :root {
    --ink: #000000;
    --paper: #ffffff;
    --title-red: #c3161d;
    --chili: #d71f1f;
    --gold-dark: #8a6a1f;
    --gold: #d9b04a;
    --gold-light: #f3d98a;
    --frame: #b8a47a;
    --frame-dark: #5e4f33;
  }
  * { margin: 0; padding: 0; box-sizing: border-box; }
  html, body { width: 935px; height: 1200px; overflow: hidden; background: var(--paper); }
  .menu-page {
    position: relative; width: 935px; height: 1200px; background: var(--ink);
    font-family: "Arimo", Arial, sans-serif; color: var(--paper); overflow: hidden;
  }
  .frame-band {
    position: absolute; inset: 14px; border: 10px solid var(--frame-dark);
    outline: 1px solid var(--frame); outline-offset: -1px;
  }
  .frame-line { position: absolute; inset: 27px; border: 1px solid var(--frame); }
  .corner {
    position: absolute; width: 56px; height: 56px;
    background: radial-gradient(circle at center, #8f7a4c, #3d3322 75%);
  }
  .corner.tl { left: 14px; top: 14px; } .corner.tr { right: 14px; top: 14px; }
  .corner.bl { left: 14px; bottom: 14px; } .corner.br { right: 14px; bottom: 14px; }
  .brand {
    position: absolute; top: 12px; left: 50%; transform: translateX(-50%);
    padding: 4px 8px; background: var(--ink);
    font-size: 12px; color: var(--title-red);
    display: flex; align-items: center; gap: 6px; white-space: nowrap;
  }
  .brand-dot { width: 30px; height: 30px; border-radius: 50%; background: var(--title-red); }
  .section-title {
    position: absolute; top: 72px; left: 0; width: 100%; text-align: center;
    font-family: "Cinzel", "Times New Roman", serif; font-weight: 700;
    font-size: 50px; letter-spacing: 1px; color: var(--title-red);
  }
  .divider {
    position: absolute; left: 52px; width: 842px; height: 6px;
    background: linear-gradient(180deg, var(--gold-dark), var(--gold-light) 50%, var(--gold-dark));
  }
  .item { position: absolute; height: 110px; }
  .item.left { left: 54px; width: 430px; }
  .item.right { left: 485px; width: 420px; }
  .photo { position: absolute; left: 0; top: 0; width: 162px; height: 108px; }
  .item-text { position: absolute; left: 166px; width: 262px; }
  .item.right .item-text { left: 171px; width: 240px; }
  .item.right .item-text.tight { left: 166px; }
  .item-name {
    font-size: 17px; line-height: 20px; font-weight: 400;
    display: flex; align-items: center; gap: 4px; white-space: nowrap;
  }
  .item-name .count { font-size: 15px; }
  .item-desc { font-size: 13.5px; line-height: 17.5px; white-space: nowrap; }
  .price { position: absolute; font-size: 14px; line-height: 16px; white-space: nowrap; }
  .item.left .price { left: 355px; }
  .item.right .price { left: 330px; }
  .item.left .price.addon { left: 173px; }
</style>
</head>
<body>
<main class="menu-page">
  <div class="frame-band" role="img" aria-label="Ornamental patterned border"></div>
  <div class="frame-line"></div>
  <div class="corner tl" role="img" aria-label="Ornamental corner scroll"></div>
  <div class="corner tr" role="img" aria-label="Ornamental corner scroll"></div>
  <div class="corner bl" role="img" aria-label="Ornamental corner scroll"></div>
  <div class="corner br" role="img" aria-label="Ornamental corner scroll"></div>

  <div class="brand"><span class="brand-dot"></span><span>Lanternleaf</span></div>
  <h1 class="section-title">APPETIZERS</h1>

  <!-- Row 1 -->
  <article class="item left" style="top:148px">
    <div class="photo" role="img" aria-label="Photo of scallion pancakes on a white plate" style="background:linear-gradient(135deg,#6b5a40,#c8a070 55%,#e8e2d8)"></div>
    <div class="item-text" style="top:14px"><h2 class="item-name">Scallion Pancakes</h2>
      <p class="item-desc">Traditional Chinese flatbread<br>folded with oil and minced<br>scallions and pan fried</p></div>
    <span class="price" style="top:96px">$6.00</span>
  </article>
  <article class="item right" style="top:148px">
    <div class="photo" role="img" aria-label="Photo of mala beef jerky on a white plate" style="background:linear-gradient(135deg,#3a3a3a,#e8e6e2 45%,#2a1c18 70%,#d8d0c8)"></div>
    <div class="item-text tight" style="top:14px"><h2 class="item-name">Crispy Mala Beef Jerky
      <svg width="36" height="14" viewBox="0 0 36 14" role="img" aria-label="Spicy"><ellipse cx="8" cy="8" rx="8" ry="4" fill="var(--chili)"/><ellipse cx="26" cy="8" rx="8" ry="4" fill="var(--chili)"/></svg></h2>
      <p class="item-desc">Dry fried shredded beef with<br>various peppersin sesame<br>and peppercorn oil</p></div>
    <span class="price" style="top:96px">$9.00</span>
  </article>
  <div class="divider" style="top:264px"></div>

  <!-- Row 2 -->
  <article class="item left" style="top:275px">
    <div class="photo" role="img" aria-label="Photo of lettuce wraps with seasoned chicken" style="background:linear-gradient(135deg,#1d1d1d,#e4e0da 30%,#6a3a24 50%,#b8d8a0 80%)"></div>
    <div class="item-text" style="top:25px"><h2 class="item-name">Lanternleaf Lettuce Wraps</h2>
      <p class="item-desc">Seasoned ground chicken drizzled<br>with our top secret homemade sauce<br>served with lettuce wraps</p></div>
    <span class="price" style="top:96px">$8.00</span>
  </article>
  <article class="item right" style="top:275px">
    <div class="photo" role="img" aria-label="Photo of fried chicken dumplings on a white plate" style="background:linear-gradient(135deg,#2a2a2a,#e6e2dc 35%,#c89850 60%,#e6e2dc)"></div>
    <div class="item-text" style="top:29px"><h2 class="item-name">Fried Chicken Dumplings <span class="count">(6)</span></h2>
      <p class="item-desc">Chinese dumpling filled with<br>Chicken, Shittake mushrooms,<br>and bamboo shoots</p></div>
    <span class="price" style="top:96px">$6.00</span>
  </article>
  <div class="divider" style="top:392px"></div>

  <!-- Row 3 -->
  <article class="item left" style="top:403px">
    <div class="photo" role="img" aria-label="Photo of salt and pepper calamari in a bowl" style="background:linear-gradient(135deg,#44505a,#e8e4dc 40%,#c89a5a 60%,#5a6a78)"></div>
    <div class="item-text" style="top:29px"><h2 class="item-name">Salt &amp; Pepper Calamari</h2>
      <p class="item-desc">Crispy Calamari with green<br>&amp; red peppers and onions</p></div>
    <span class="price" style="top:92px">$9.00</span>
  </article>
  <article class="item right" style="top:403px">
    <div class="photo" role="img" aria-label="Photo of dumplings in red oil sauce" style="background:linear-gradient(135deg,#48525a,#e8e4dc 40%,#c04a20 60%,#6a7078)"></div>
    <div class="item-text" style="top:24px"><h2 class="item-name">Red Oil Dumpling <span class="count">(6)</span>
      <svg width="30" height="14" viewBox="0 0 30 14" role="img" aria-label="Spicy"><ellipse cx="18" cy="8" rx="9" ry="4" fill="var(--chili)"/></svg></h2>
      <p class="item-desc">Chicken filled dumplings in<br>Sichuan red oil sauce<br>drizzled with sesame</p></div>
    <span class="price" style="top:92px">$7.00</span>
  </article>
  <div class="divider" style="top:517px"></div>

  <!-- Row 4 -->
  <article class="item left" style="top:532px">
    <div class="photo" role="img" aria-label="Photo of bang shrimp in a white bowl" style="background:linear-gradient(135deg,#d8d2c8,#f2eee8 40%,#c05830 60%,#e0dad0)"></div>
    <div class="item-text" style="top:26px"><h2 class="item-name">Buddha Bang Shrimp</h2>
      <p class="item-desc">Crispy fried shrimp tossed in our<br>creamy spicy sauce</p></div>
    <span class="price" style="top:92px">$9.00</span>
  </article>
  <article class="item right" style="top:532px">
    <div class="photo" role="img" aria-label="Photo of vegetarian spring rolls with chili dip" style="background:linear-gradient(135deg,#d8d4cc,#f4f2ee 45%,#d8b870 65%,#eceae4)"></div>
    <div class="item-text" style="top:30px"><h2 class="item-name">Vegetarian Spring Rolls <span class="count">(3)</span></h2>
      <p class="item-desc">Traditional &nbsp;Asian Roll served<br>with a sweet chili sauce</p></div>
    <span class="price" style="top:92px">$4.00</span>
  </article>
  <div class="divider" style="top:646px"></div>

  <!-- Row 5 -->
  <article class="item left" style="top:660px">
    <div class="photo" role="img" aria-label="Photo of drunken chicken in a white bowl" style="background:linear-gradient(135deg,#bcb6ac,#eeeae4 40%,#b0603a 60%,#d0cac0)"></div>
    <div class="item-text" style="top:24px"><h2 class="item-name">Drunken Chicken</h2>
      <p class="item-desc">Chicken, Thai chili in a house maple<br>spicy sauce</p></div>
    <span class="price" style="top:90px">$8.00</span>
  </article>
  <article class="item right" style="top:660px">
    <div class="photo" role="img" aria-label="Photo of garlic cucumber salad in a dark dish" style="background:linear-gradient(135deg,#cfc8bc,#2a2a2a 45%,#7ab060 65%,#e0dace)"></div>
    <div class="item-text" style="top:24px"><h2 class="item-name">Garlic Cucumber Salad</h2>
      <p class="item-desc">Sliced cucumber with a garlic<br>vinaigrette</p></div>
    <span class="price" style="top:93px">$4.00</span>
  </article>
  <div class="divider" style="top:771px"></div>

  <!-- Row 6 -->
  <article class="item left" style="top:788px">
    <div class="photo" role="img" aria-label="Photo of Sichuan spiced beef in a red bowl" style="background:linear-gradient(135deg,#3a3a3a,#c41e1e 40%,#e8d8c0 55%,#a81a1a)"></div>
    <div class="item-text" style="top:25px"><h2 class="item-name">Sichaun Spiced Beef</h2>
      <p class="item-desc">Beef Shank, beef tripe, cilantro,<br>peanuts and celery</p></div>
    <span class="price" style="top:87px">$9.00</span>
  </article>
  <article class="item right" style="top:788px">
    <div class="photo" role="img" aria-label="Photo of hot and sour soup in a bowl" style="background:linear-gradient(135deg,#6a5038,#c06020 45%,#d88a40 60%,#5a4430)"></div>
    <div class="item-text" style="top:13px"><h2 class="item-name">Hot n’ Sour Soup
      <svg width="30" height="14" viewBox="0 0 30 14" role="img" aria-label="Spicy"><ellipse cx="18" cy="8" rx="9" ry="4" fill="var(--chili)"/></svg></h2>
      <p class="item-desc">Tangy broth with bamboo<br>shoots,wood ear mushrooms,<br>tofu, egg and carrots</p></div>
    <span class="price" style="top:87px">$7.00</span>
  </article>
  <div class="divider" style="top:896px"></div>

  <!-- Row 7 -->
  <article class="item left" style="top:908px">
    <div class="photo" role="img" aria-label="Photo of crispy bottom bao buns on a white plate" style="background:linear-gradient(135deg,#3a5a6a,#f0ece4 40%,#e6e0d4 60%,#c06030)"></div>
    <div class="item-text" style="top:1px"><h2 class="item-name">Beef Crispy Bottom Bao
      <svg width="50" height="14" viewBox="0 0 50 14" role="img" aria-label="Spicy"><ellipse cx="18" cy="8" rx="9" ry="4" fill="var(--chili)"/><ellipse cx="39" cy="8" rx="9" ry="4" fill="var(--chili)"/></svg></h2>
      <p class="item-desc">Pan fried crispy bottom Bao, stuffed<br>with beef drizzled with scallion and<br>sesame (Fresh madeto order, takes<br>at least 20 mins to serve)</p></div>
    <span class="price addon" style="top:98px">add Shrimp &nbsp;$1.00</span>
    <span class="price" style="top:98px">$10.00</span>
  </article>
  <article class="item right" style="top:908px">
    <div class="photo" role="img" aria-label="Photo of West Lake soup in a bowl" style="background:linear-gradient(135deg,#8a8a86,#c8c0a8 40%,#a8a890 60%,#6a6a66)"></div>
    <div class="item-text" style="top:1px"><h2 class="item-name">West Lake Soup</h2>
      <p class="item-desc">Light creamy soup with<br>ground beef, diced Shitake<br>mushrooms, tofu, bamboo<br>shoots, egg white, and<br>cilantro</p></div>
    <span class="price" style="top:98px">$4.00</span>
  </article>
  <div class="divider" style="top:1022px"></div>

  <!-- Row 8 -->
  <article class="item left" style="top:1070px">
    <div class="item-text" style="top:8px"><h2 class="item-name">Edamame</h2>
      <p class="item-desc">Season and boiled soya bean</p></div>
    <span class="price" style="top:55px">$4.00</span>
  </article>
  <article class="item right" style="top:1051px">
    <div class="item-text" style="top:0"><h2 class="item-name">Pork Egg Rolls <span class="count">(2)</span></h2>
      <p class="item-desc">Handrolled with julienned<br>veggies with our sweet n’<br>sour mustard sauce</p></div>
    <span class="price" style="top:77px">$4.00</span>
  </article>
</main>
</body>
</html>
```